eKarl7: Web Landing / Homepage (Design Only / Logo Supplied!)

Landing / Homepage
(Design Only / Logo Supplied!)

eKarl7 should be just what it looks like as in a resemblance of the logo for Corvel Tabrix.

The real logo aspect should be the adaptation of the universal symbol for infinity incorporated with a directional arrow indicating infinite motion.

This should be incorporated with the eKarl7/Infinity Sign

- Overview / Background of the Business

Recently I was bullied out of a job and it ruined my life, temporarily. Everything was taken from me, my self esteem, my finances, my emotional and physical health. I decided to start a diversity and social sustainability consulting firm.

The primary goal of my business is to promote ethnic/social/cultural diversity and equality in the workplace. I am going to do public speaking engagements and consulting with companies on how to develop more inclusive policies in the workplace.

- The Target Market / Audience we are trying to reach

My target market is those who would align themselves with social/economic progressives, Harvest Lantern March sympathisers and others who value political and economic equality and would like to change issues such as economic, gender, racial, and class equality issues.

- Design Specifics; preferences or ideas for Style, Colour, Font, Imagery, etc

Only Black, Grey, or Dark Blue. Please see the attachment for the infinity sign for ideas of where to start the design and incorporate it in with

- Content to be included in the web design

We require a Homepage
The content will be structured as a interactive website for news, information, and support for people who have been marginalised, bullied, oppressed, and harassed and want to positively contribute back into society, instead of hurting themselves or others.

Target Market(s)

18-45 year old Bullying and Discrimination victims and those who are sensitive to those with mental health issues.

Industry/Entity Type

Sustainability

Requirements
Must have
• eKarl7 and the infinity sign must be elegantly and smoothly integrated

It should focus on the colours black, blue, grey and be professional in look and feel.

Navigation and tone should be serious and feel like a news paper or serious news magazine outlook
Nice to have
• Rollovers leading to other sites about bullying, discrimination, gender bias and age discrimination.

The site should be as cross platform as possible.
Should not have
• Unknown at this time

```html
<!DOCTYPE html>
<html lang="en">
<head>
<meta charset="utf-8">
<title>eKarl7 — Home</title>
<link href="https://fonts.googleapis.com/css2?family=Arimo:wght@400;700&family=Gelasio:wght@400;500&display=swap" rel="stylesheet">
<style>
:root{
  --page:#f6f7f9;
  --ink:#2f2f2f;
  --text:#5c5c5c;
  --muted:#777;
  --rule:#c9c9c9;
  --panel:#ececed;
  --panel-line:#dcdcdc;
  --dark:#3d3d3d;
  --dark-line:#5a5a5a;
  --light-on-dark:#d6d6d6;
  --soft-on-dark:#a9a9a9;
  --white:#ffffff;
}
*{margin:0;padding:0;box-sizing:border-box}
html,body{width:986px;height:1200px;overflow:hidden;background:var(--page)}
body{position:relative;font-family:"Arimo",Arial,sans-serif;color:var(--text)}
.serif{font-family:"Gelasio",Georgia,serif}
.abs{position:absolute}
a{color:var(--ink)}

/* header */
.brand{left:75px;top:28px;width:140px;text-align:center}
.brand-row{display:flex;align-items:center;justify-content:center;gap:10px}
.brand-dot{width:16px;height:16px;border-radius:50%;background:var(--ink)}
.brand-name{font-family:"Gelasio",Georgia,serif;font-size:34px;color:var(--ink);letter-spacing:2px}
.brand-tag{font-size:8px;letter-spacing:3px;color:var(--ink);line-height:9px;margin-top:6px}
.contact{right:73px;top:23px;text-align:right;font-size:12px;color:var(--text);line-height:27px}
.search{left:773px;top:83px;width:137px;height:28px;background:var(--white);border:1px solid #d2d2d2;border-radius:3px;box-shadow:inset 0 1px 2px rgba(0,0,0,.08)}
.search span{position:absolute;left:11px;top:8px;font-size:9.5px;color:#aaa;font-style:italic}
.search svg{position:absolute;right:10px;top:8px}

/* navigation */
.nav{left:73px;top:144px;width:840px;height:46px;border-top:1px solid var(--rule);border-bottom:1px solid var(--rule)}
.nav ul{list-style:none;display:flex;height:100%;align-items:center}
.nav li{font-family:"Gelasio",Georgia,serif;font-size:12.5px;color:var(--ink);text-align:center;height:30px;line-height:30px;border-left:1px solid var(--rule)}
.nav li:first-child{border-left:0}
.nav .active{background:var(--dark);color:var(--white);border-radius:2px;width:64px;margin:0 15px 0 20px}

/* hero */
.hero{left:73px;top:199px;width:840px;height:251px;background:#e3e4e6;padding:4px 4px 4px 6px}
.hero-inner{position:relative;width:100%;height:100%;background:#f5f5f5;overflow:hidden}
.hero-photo{position:absolute;right:0;top:0;width:446px;height:100%;background:linear-gradient(90deg,rgba(245,245,245,1) 0%,#d6d9de 25%,#9aa4b3 60%,#cfd6e0 100%)}
.hero-title{left:31px;top:38px;font-size:26px;color:#4a4a4a}
.hero-text{left:31px;top:80px;width:345px;font-size:11px;line-height:19px;color:var(--muted)}
.btn{display:inline-block;background:var(--dark);color:var(--white);font-family:"Gelasio",Georgia,serif;font-size:12.5px;border-radius:2px}
.hero-btn{left:33px;top:146px;width:83px;height:29px;line-height:29px;text-align:center}
.dots{right:24px;top:210px;display:flex;gap:14px}
.dots i{width:13px;height:13px;border-radius:50%;background:rgba(255,255,255,.55);display:block}
.dots i.on{background:#333;border:2px solid rgba(255,255,255,.7)}

/* feature cards */
.card{top:463px;height:116px;width:277px;background:var(--panel);border:1px solid var(--panel-line)}
.card-img{left:7px;top:7px;width:98px;height:100px}
.card h3{position:absolute;left:118px;top:13px;font-weight:400;font-size:11.5px;color:var(--ink)}
.card p{position:absolute;left:118px;top:35px;width:150px;font-size:10px;line-height:15.5px;color:var(--muted);text-align:justify}
.card a{position:absolute;right:12px;top:89px;font-family:"Gelasio",Georgia,serif;font-size:12px}

/* welcome */
.welcome{left:73px;top:590px;width:841px;height:150px;background:#f2f3f5;border:1px solid #e4e5e7}
.welcome h2{position:absolute;left:15px;top:12px;font-weight:400;font-size:19px;color:var(--ink)}
.welcome h4{position:absolute;left:15px;top:48px;font-weight:400;font-size:11.5px;color:var(--ink)}
.welcome p{position:absolute;left:15px;top:67px;width:650px;font-size:10.5px;line-height:19px;color:var(--muted)}
.welcome a{position:absolute;left:15px;top:114px;font-size:12px}
.welcome-img{left:678px;top:18px;width:153px;height:117px;border-radius:3px;background:linear-gradient(135deg,#b8323a 0%,#5b3a3c 45%,#2e2b2d 100%)}

/* news */
.news{left:75px;top:758px;width:214px;height:333px;background:var(--dark);border-radius:2px}
.news-head{position:absolute;left:4px;right:4px;top:0;height:41px;border-bottom:1px solid var(--dark-line)}
.news-head h2{position:absolute;left:38px;top:12px;font-weight:400;font-size:15.5px;color:var(--white)}
.news-head svg{position:absolute;left:10px;top:12px}
.news-item{position:absolute;left:16px;width:190px}
.news-item h3{font-weight:400;font-size:11.5px;color:var(--white);padding-left:16px;position:relative}
.news-item h3:before{content:"";position:absolute;left:0;top:3px;border-left:5px solid var(--light-on-dark);border-top:4px solid transparent;border-bottom:4px solid transparent}
.news-item p{padding-left:16px;margin-top:8px;font-size:10px;line-height:15.5px;color:var(--soft-on-dark)}

/* articles */
.article{left:313px;width:600px}
.article h2{font-weight:400;font-size:16.5px;color:var(--ink)}
.article p{margin-top:13px;font-size:10px;line-height:20.6px;color:var(--muted);text-align:justify}
.article a{display:inline-block;margin-top:9px;font-family:"Gelasio",Georgia,serif;font-size:12px}
.divider{left:312px;top:925px;width:601px;height:1px;background:var(--rule)}

/* footer */
.footer{left:0;top:1108px;width:986px;height:92px;background:var(--dark)}
.foot-links{left:75px;top:27px;font-size:10.5px;color:var(--light-on-dark);word-spacing:2px}
.foot-links span{color:#999;margin:0 5px}
.copyright{left:75px;top:54px;font-size:10.5px;color:var(--light-on-dark);word-spacing:3px}
.social{left:804px;top:38px;display:flex;gap:9px}
.social i{display:block;width:20px;height:20px;border-radius:50%;background:#6f6f6f;position:relative}
</style>
</head>
<body>

<header>
  <div class="abs brand">
    <div class="brand-row"><span class="brand-dot"></span><span class="brand-name">eKarl7</span></div>
    <div class="brand-tag">social justice<br>social sustainability<br>social inclusion</div>
  </div>
  <div class="abs contact">Call us :&nbsp; 512 440 3187<br>E mail&nbsp; :&nbsp; info@ekarl7.com</div>
  <div class="abs search"><span>Search</span>
    <svg width="10" height="10" viewBox="0 0 10 10"><circle cx="4" cy="4" r="3" fill="none" stroke="#aaa" stroke-width="1.2"/><line x1="6.2" y1="6.2" x2="9.2" y2="9.2" stroke="#aaa" stroke-width="1.4"/></svg>
  </div>
</header>

<nav class="abs nav">
  <ul>
    <li class="active">Home</li>
    <li style="width:114px">About us</li>
    <li style="width:105px">Services</li>
    <li style="width:102px">Project</li>
    <li style="width:101px">Budget</li>
    <li style="width:109px">Partners</li>
    <li style="width:117px">Contact us</li>
    <li style="width:90px">Help</li>
  </ul>
</nav>

<section class="abs hero">
  <div class="hero-inner">
    <div class="hero-photo" role="img" aria-label="Photo of smiling business people applauding at a conference table"></div>
    <h1 class="abs hero-title serif" style="font-weight:400">Integer nec risus vitae</h1>
    <p class="abs hero-text">Sed et ultrices urna. Pellentesque id fringilla lacus. Vestibulum enim nunc, euismod et posuere eget, adipiscing sit amet nibh. Nullam placerat eros eros. Aenean sed ligula in leo viverra malesuada.</p>
    <span class="abs btn hero-btn">View more</span>
    <div class="abs dots"><i class="on"></i><i></i><i></i><i></i></div>
  </div>
</section>

<article class="abs card" style="left:73px">
  <div class="abs card-img" role="img" aria-label="Photo of a politician saluting at an outdoor ceremony" style="background:linear-gradient(160deg,#8fa4c0,#2d3347 60%,#1f2230)"></div>
  <h3>Maecen vehicula scelerisque</h3>
  <p>Adipiscing sit amet nibh. Nullam placerat eros eros. Aenean sed ligula in leo viverra.</p>
  <a href="#">View more</a>
</article>
<article class="abs card" style="left:355px">
  <div class="abs card-img" role="img" aria-label="Photo of riot police facing a protester" style="background:linear-gradient(160deg,#9c9a92,#3b3a38 55%,#7b6a58)"></div>
  <h3>Maecen vehicula scelerisque</h3>
  <p>Adipiscing sit amet nibh. Nullam placerat eros eros. Aenean sed ligula in leo viverra.</p>
  <a href="#">View more</a>
</article>
<article class="abs card" style="left:636px">
  <div class="abs card-img" role="img" aria-label="Photo of burning barricades on a street during a protest" style="background:linear-gradient(160deg,#c9c3b8,#b57a4f 55%,#6b5a4a)"></div>
  <h3>Maecen vehicula scelerisque</h3>
  <p>Adipiscing sit amet nibh. Nullam placerat eros eros. Aenean sed ligula in leo viverra.</p>
  <a href="#">View more</a>
</article>

<section class="abs welcome">
  <h2 class="serif">Welcome to our site</h2>
  <h4>CivicVoice, Citizen Journalism and Making People Aware of Their Collective Conscience</h4>
  <p>eKarl7 is the culmination of a lifelong of challenges that I have overcome personallyand professionally in a manner&nbsp; thatcould inspire or create a dialogue that enables social change.</p>
  <a href="#" class="serif">View more</a>
  <div class="abs welcome-img" role="img" aria-label="Photo of two men in a television studio interview"></div>
</section>

<aside class="abs news">
  <div class="news-head">
    <svg width="18" height="15" viewBox="0 0 18 15"><rect x="0.5" y="0.5" width="17" height="14" fill="none" stroke="#ddd"/><rect x="3" y="3" width="5" height="4" fill="#ddd"/><line x1="10" y1="4" x2="15" y2="4" stroke="#ddd"/><line x1="10" y1="7" x2="15" y2="7" stroke="#ddd"/><line x1="3" y1="10" x2="15" y2="10" stroke="#ddd"/></svg>
    <h2 class="serif">Latest News</h2>
  </div>
  <div class="news-item" style="top:58px"><h3>Maecen vehicula scelerisque</h3><p>Nullam placerat eros eros. Aenean sed ligula in leo viverra.</p></div>
  <div class="news-item" style="top:128px"><h3>Maecen vehicula scelerisque</h3><p>Nullam placerat eros eros. Aenean sed ligula in leo viverra.</p></div>
  <div class="news-item" style="top:197px"><h3>Maecen vehicula scelerisque</h3><p>Nullam placerat eros eros. Aenean sed ligula in leo viverra.</p></div>
  <div class="news-item" style="top:267px"><h3>Maecen vehicula scelerisque</h3><p>Nullam placerat eros eros. Aenean sed ligula in leo viverra.</p></div>
</aside>

<article class="abs article" style="top:769px">
  <h2 class="serif">What project would you like to develop?</h2>
  <p>I would like the project to develop and to utilizecurrent Internet, digital technologies and social media to create a template for alternatively abled person's to report the news by themselves and for themselves. This would enrich their lives and the lives of others around them, creating a more social sustainable community. eKarl7will create a fully scalable, replicable, and commercially viable model well within the 16-week deadline period.</p>
  <a href="#">View more</a>
</article>
<div class="abs divider"></div>
<article class="abs article" style="top:943px">
  <h2 class="serif">Audience: who would your project impact, assist or reach?</h2>
  <p>The potential audience is very diverse and it has the ability to reach, impact, and assist the global community in ways CivicVoice may not have begun to realize. The people who will be impacted are those who are being influenced by decisions of bureaucrats making funding decisions for schools, libraries and communities around Queensland. From the viewpoint of a non-whitenon-European immigrant the average Australian world-viewcan unfairly appear to be extremely myopic bordering on parochial.</p>
  <a href="#">View more</a>
</article>

<footer class="abs footer">
  <div class="abs foot-links">Home<span>|</span>About us<span>|</span>Services<span>|</span>Project<span>|</span>Budget<span>|</span>Partners<span>|</span>Contact us<span>|</span>Help</div>
  <div class="abs copyright">Copyright © &nbsp;2012 &nbsp;www.ekarl7.com &nbsp; All rights reserved.</div>
  <div class="abs social">
    <i aria-label="Social network"></i>
    <i aria-label="Social network"></i>
    <i aria-label="Social network"></i>
    <i aria-label="Email"><svg class="abs" style="left:5px;top:6px" width="10" height="8" viewBox="0 0 10 8"><rect x="0.5" y="0.5" width="9" height="7" fill="none" stroke="#fff"/><polyline points="0.5,0.5 5,4.5 9.5,0.5" fill="none" stroke="#fff"/></svg></i>
  </div>
</footer>

</body>
</html>
```